MIRA TOLLEN'S Gingerbeer beverages needs a logo design for a our label.

Mira Tollen is the name of my ginger beer. the font I would like use for MIRA TOLLEN is Emperator hand Ess and a script for Ginger beer. the label will be printed on clear vinyl. Its a Extra Spicy from 700 year old recipe. We make it with a wild probiotic. The finial design should create a thirst for great tasting product have a simple image that reflect nature of the ginger planet. Colors can be bright red like maroon and gold. Business is in Texas.

```html
<!DOCTYPE html>
<html lang="en">
<head>
<meta charset="utf-8">
<title>Mira Tollen Ginger Beer Label</title>
<link rel="stylesheet" href="https://fonts.googleapis.com/css2?family=Marcellus&family=Source+Serif+4:opsz,wght@8..60,700&family=Great+Vibes&display=swap">
<style>
  :root {
    --canvas: #ffffff;
    --label: #e9e6da;
    --maroon: #a51c24;
    --maroon-deep: #7d1418;
    --gold: #a8782c;
    --gold-bright: #d9b23e;
    --gold-soft: #f0dc9a;
  }
  html, body {
    margin: 0;
    width: 1200px;
    height: 1200px;
    overflow: hidden;
    background: var(--canvas);
  }
  .label {
    position: absolute;
    left: 240px;
    top: 60px;
    width: 720px;
    height: 1080px;
    background: var(--label);
    border-radius: 28px;
    overflow: hidden;
    text-align: center;
  }
  .tagline {
    position: absolute;
    top: 150px;
    left: 0;
    right: 0;
    margin: 0;
    font-family: "Source Serif 4", Georgia, serif;
    font-weight: 700;
    font-size: 30px;
    color: var(--gold);
  }
  .ginger-sprig {
    position: absolute;
    top: 205px;
    left: 285px;
    width: 150px;
    height: 90px;
    border-radius: 40px;
    background: radial-gradient(ellipse at center, #d8bd94 0%, rgba(216,189,148,0.25) 70%, transparent 100%);
  }
  .brand-name {
    position: absolute;
    top: 310px;
    left: 0;
    right: 0;
    margin: 0;
    font-family: "Marcellus", "Times New Roman", serif;
    font-weight: 400;
    font-size: 72px;
    letter-spacing: 2px;
    color: var(--maroon);
    line-height: 1;
  }
  .product-type {
    position: absolute;
    top: 385px;
    left: 0;
    right: 0;
    margin: 0;
    font-family: "Great Vibes", cursive;
    font-size: 56px;
    color: var(--gold);
    line-height: 1;
  }
  .flavour {
    position: absolute;
    top: 480px;
    left: 0;
    right: 0;
    margin: 0;
    font-family: "Source Serif 4", Georgia, serif;
    font-weight: 700;
    font-size: 27px;
    color: var(--maroon);
  }
  .ginger-root {
    position: absolute;
    top: 560px;
    left: 0;
    width: 720px;
    height: 380px;
    border-radius: 160px 40px 120px 60px;
    background: radial-gradient(ellipse at 62% 55%, var(--gold-bright) 0%, var(--gold-soft) 45%, rgba(240,220,154,0.2) 80%, transparent 100%);
  }
  .volume {
    position: absolute;
    top: 975px;
    left: 0;
    right: 0;
    margin: 0;
    font-family: "Source Serif 4", Georgia, serif;
    font-weight: 700;
    font-size: 27px;
    color: var(--gold);
  }
</style>
</head>
<body>
  <main class="label">
    <p class="tagline">Wild Probiotic</p>
    <div class="ginger-sprig" role="img" aria-label="Small gold line drawing of a ginger root with leaves"></div>
    <h1 class="brand-name">MIRA TOLLEN</h1>
    <p class="product-type">Ginger beer</p>
    <p class="flavour">Extra Spicy</p>
    <div class="ginger-root" role="img" aria-label="Large gold line illustration of a ginger root with leaves"></div>
    <p class="volume">32 fl oz</p>
  </main>
</body>
</html>
```